Financial Advisor needs waiting room sign

I am a financial advisor that works with a number of accountants to develop prospects. I am looking for a 18"x24" sign to hang in their office waiting rooms to help develop prospect interest in my services. My original idea was to list all of our services in a jumbled way on the sign and on the bottom have something like "Confused? We have the answers?" "Questions - We have answers" Our logo on the bottom. While I think this is still a good idea when I try to design it - it does not work. I am open to other ideas. Here is a list of our services (list in no particular order) and I will attach our logo. List: Vellorin, Vellorin Supplement, Vellorin Advantage, Tolquist, Part A, Part B, Part D, Social Security, Turning 65, Annuities, Fixed Index Annuities, Rollovers, 401k, 403b, Investments, Stock Market, Mutual Funds, Term Insurance, Life Insurance, Final Expense, Long Term Care, Mortgage Protection, 403B / 457 Not for Profit Set Up, 403B / TSA Plans, Annuities, Asset Protection, Charitable Giving, College Funding, Estate Planning, Fixed Indexed Annuities, Guaranteed Income, IRA & 401(K) Assets and Planning, IRA, 401(K), 403(B) Rollovers, Lifetime Income Planning, Retirement Income Planning, Safe Money Options, Social Security, Tactical Asset Allocation

```html
<!DOCTYPE html>
<html lang="en">
<head>
<meta charset="utf-8">
<title>Brackwell Capital – Waiting Room Sign</title>
<link href="https://fonts.googleapis.com/css2?family=Saira+Semi+Condensed:wght@500;700;800&display=swap" rel="stylesheet">
<style>
  :root {
    --green: #6ea30a;
    --green-dark: #4b6e0c;
    --charcoal: #464646;
    --ink: #3a3a3a;
    --white: #ffffff;
    --mist: #d9d9d9;
  }
  * { margin: 0; padding: 0; box-sizing: border-box; }
  html, body { width: 994px; height: 1200px; overflow: hidden; background: var(--white); }
  body { font-family: "Saira Semi Condensed", Arial, sans-serif; color: var(--ink); }
  .sign { position: relative; width: 994px; height: 1200px; overflow: hidden; background: var(--white); }
  .backdrop { position: absolute; inset: 0; }

  .brand { position: absolute; top: 78px; left: 48px; display: flex; align-items: center; gap: 26px; }
  .brand-dot { width: 104px; height: 104px; border-radius: 50%; background: var(--green); flex: none; }
  .brand-name { font-weight: 800; font-size: 62px; line-height: 1; letter-spacing: 3px; color: var(--green-dark); text-transform: uppercase; }
  .brand-tag { margin-top: 8px; font-weight: 700; font-size: 22px; letter-spacing: 5px; color: var(--ink); text-transform: uppercase; }

  .headline { position: absolute; top: 380px; left: 0; width: 560px; text-align: center; }
  .headline h1 { font-weight: 800; font-size: 92px; line-height: 1; color: var(--green); }
  .headline p { font-weight: 700; font-size: 26px; color: var(--green); margin-top: 2px; }

  .scene-art { position: absolute; left: 30px; top: 620px; width: 580px; height: 400px;
    background: linear-gradient(180deg, #4d4d4d 0%, #6a5a55 70%, #b8695a 100%); border-radius: 6px; }

  .services { position: absolute; top: 300px; left: 655px; width: 320px; color: var(--white); }
  .services h2 { font-weight: 800; font-size: 50px; line-height: 1; }
  .services .rule { width: 52px; height: 5px; background: var(--white); margin: 8px 0 14px; }
  .services ul { list-style: none; }
  .services li { font-weight: 700; font-size: 14px; line-height: 16px; padding-left: 12px; position: relative; }
  .services li::before { content: ""; position: absolute; left: 0; top: 6px; width: 6px; height: 6px; border-radius: 50%; background: var(--ink); }

  .contact { position: absolute; left: 0; right: 0; top: 1065px; text-align: center; }
  .contact .prompt { display: inline-flex; align-items: center; gap: 10px; font-weight: 700; font-size: 34px; color: var(--ink); }
  .contact .prompt::before, .contact .prompt::after { content: ""; width: 80px; height: 4px; background: var(--green); }
  .contact .phone { font-weight: 800; font-size: 86px; line-height: 1; color: var(--green); margin-top: 2px; }
</style>
</head>
<body>
<main class="sign">
  <svg class="backdrop" width="994" height="1200" viewBox="0 0 994 1200" aria-hidden="true">
    <rect class="panel-dark" x="0" y="250" width="994" height="800" fill="var(--charcoal)"/>
    <path class="header-curve" d="M0 0 H994 V218 C760 290 420 300 0 250 Z" fill="var(--white)"/>
    <path class="header-shade" d="M0 250 C420 300 760 290 994 218 V230 C760 302 420 312 0 262 Z" fill="var(--mist)"/>
    <path class="panel-green" d="M994 210 C870 260 760 285 640 295 C590 480 590 800 640 1030 L994 1070 Z" fill="var(--green)"/>
    <path class="footer-curve" d="M0 1040 C300 1000 700 1010 994 1072 V1200 H0 Z" fill="var(--white)"/>
    <path class="footer-shade" d="M0 1030 C300 990 700 1000 994 1062 V1072 C700 1010 300 1000 0 1040 Z" fill="var(--mist)"/>
    <g class="thought-cloud" fill="var(--white)">
      <ellipse cx="180" cy="450" rx="150" ry="72"/>
      <ellipse cx="300" cy="400" rx="140" ry="80"/>
      <ellipse cx="420" cy="460" rx="130" ry="78"/>
      <ellipse cx="330" cy="500" rx="150" ry="70"/>
    </g>
  </svg>

  <header class="brand">
    <span class="brand-dot"></span>
    <div>
      <div class="brand-name">Brackwell Capital</div>
      <div class="brand-tag">Insurance and Financial Services</div>
    </div>
  </header>

  <section class="headline">
    <h1>Confused?</h1>
    <p>We have the answers?</p>
  </section>

  <div class="scene-art" role="img" aria-label="Illustration of a puzzled man and woman surrounded by floating question marks"></div>

  <section class="services">
    <h2>SERVICES</h2>
    <div class="rule"></div>
    <ul>
      <li>Vellorin</li><li>Vellorin Supplement</li><li>Vellorin Advantage</li><li>Tolquist</li>
      <li>Part A</li><li>Part B</li><li>Part D</li><li>Social Security</li><li>Turning 65,</li>
      <li>Annuities</li><li>Fixed Index Annuities</li><li>Rollovers</li><li>401k</li><li>403b</li>
      <li>Investments</li><li>Stock Market</li><li>Mutual Funds</li><li>Term Insurance</li>
      <li>Life Insurance</li><li>Final Expense</li><li>Long Term Care</li><li>Mortgage Protection</li>
      <li>403B / 457 Not for Profit Set Up</li><li>403B / TSA Plans</li><li>Annuities</li>
      <li>Asset Protection</li><li>Charitable Giving</li><li>College Funding</li><li>Estate Planning</li>
      <li>Fixed Indexed Annuities</li><li>Guaranteed Income</li><li>IRA &amp; 401(K) Assets and Planning,</li>
      <li>IRA</li><li>401(K)</li><li>403(B) Rollovers</li><li>Lifetime Income Planning</li>
      <li>Retirement Income Planning</li><li>Safe Money Options</li><li>Social Security</li>
      <li>Tactical Asset Allocation</li>
    </ul>
  </section>

  <footer class="contact">
    <div class="prompt">Call us for any solutions</div>
    <div class="phone">+1-000+000+0000</div>
  </footer>
</main>
</body>
</html>
```